We need a design for our security installation based business. Our name is K M Security Systems

We need a business card for a security installation based company. We want to look modern and professional. We would like our company logo used and the three main colours to be white, black and orange. We install intruder alarms, cctv and access control. Our preference would be to use the black/orange design on the front and orange/black on the back. Feel free to post variations.

Target Market(s)

Business owners, commercial property and large residential properties

Industry/Entity Type

Business

Contact Information for Business Card

Owen Pelham 07813 592 640

Liam Fenwick 07751 286 419

operations@kmsecuritysystems.co.uk

Intruder Alarms
CCTV
Access Control

Colors
f78f20
000000
ffffff

Requirements
Must have
• Must have the logo on the business card somewhere

```html
<!DOCTYPE html>
<html lang="en">
<head>
<meta charset="utf-8">
<title>K M Security Systems – Business Cards</title>
<link rel="stylesheet" href="https://fonts.googleapis.com/css2?family=Arimo:wght@700&family=Open+Sans:wght@400&display=swap">
<style>
  :root {
    --orange: #fb4b00;
    --black: #000000;
    --white: #ffffff;
    --backdrop: #ebe8e5;
  }
  html, body {
    margin: 0;
    padding: 0;
    overflow: hidden;
  }
  .canvas {
    position: relative;
    width: 1200px;
    height: 900px;
    background: var(--backdrop);
    overflow: hidden;
  }
  .card {
    position: absolute;
    box-sizing: border-box;
  }
  .card-front {
    left: 78px;
    top: 35px;
    width: 587px;
    height: 362px;
    background: var(--orange);
    color: var(--white);
  }
  .card-back {
    left: 388px;
    top: 505px;
    width: 567px;
    height: 352px;
    background: var(--black);
  }
  .services {
    position: absolute;
    left: 32px;
    top: 40px;
    margin: 0;
    padding: 0;
    list-style: none;
    font-family: "Open Sans", sans-serif;
    font-size: 16px;
    line-height: 21.5px;
  }
  .services li {
    display: flex;
    align-items: center;
    gap: 6px;
  }
  .services li::before {
    content: "";
    width: 9px;
    height: 9px;
    border-radius: 50%;
    background: var(--white);
  }
  .contacts {
    position: absolute;
    left: 33px;
    top: 190px;
  }
  .contact-name {
    margin: 0;
    font-family: "Arimo", sans-serif;
    font-weight: 700;
    font-size: 20px;
    line-height: 26px;
    text-transform: uppercase;
  }
  .contact-phone {
    margin: 0 0 5px;
    font-family: "Open Sans", sans-serif;
    font-size: 17px;
    line-height: 25px;
  }
  .contact-email {
    margin: 6px 0 0;
    font-family: "Open Sans", sans-serif;
    font-size: 15px;
  }
  .front-brand {
    position: absolute;
    left: 300px;
    top: 0;
    width: 287px;
    height: 362px;
    display: flex;
    align-items: center;
    justify-content: center;
    margin: 0;
    font-family: "Arimo", sans-serif;
    font-weight: 700;
    font-size: 38px;
    line-height: 44px;
    text-align: center;
    text-transform: uppercase;
    color: var(--white);
  }
  .back-brand {
    position: absolute;
    inset: 0;
    display: flex;
    flex-direction: column;
    align-items: center;
    justify-content: center;
    gap: 22px;
  }
  .brand-square {
    width: 70px;
    height: 70px;
    background: var(--orange);
  }
  .brand-name {
    margin: 0;
    font-family: "Arimo", sans-serif;
    font-weight: 700;
    font-size: 34px;
    letter-spacing: 1px;
    text-transform: uppercase;
    color: var(--orange);
  }
</style>
</head>
<body>
  <main class="canvas">
    <section class="card card-front">
      <ul class="services">
        <li>Intruder Alarms</li>
        <li>CCTV</li>
        <li>Access Control</li>
      </ul>
      <div class="contacts">
        <p class="contact-name">Owen Pelham</p>
        <p class="contact-phone">07813 592 640</p>
        <p class="contact-name">Liam Fenwick</p>
        <p class="contact-phone">07751 286 419</p>
        <p class="contact-email">operations@kmsecuritysystems.co.uk</p>
      </div>
      <p class="front-brand">K M<br>Security<br>Systems</p>
    </section>

    <section class="card card-back">
      <div class="back-brand">
        <div class="brand-square"></div>
        <p class="brand-name">K M Security Systems</p>
      </div>
    </section>
  </main>
</body>
</html>
```